Open House 2017

We need a flyer for an insert for a newspaper for an open house that we are going to have and we are also wanting to list the front of the flyer the 3 pictures of our real estate agents and our Logo.

For the real estate agents : The one with Purple shirt would be the middle picture.

Attached also is our current Logo, Please re-design our Logo a bit to make it look better.

Target Market(s)

Residential and commercial and Land In our rural areas.

Industry/Entity Type

House

Requirements
Must have
• Front page -
• Our logo at the top our 3 pictures at the top after our logo and business address.
• Middle of page Some thing worded similar to the following:"let us place a SOLD sign in your front yard". Or
• " Sold vs. For Sale which would you like to see in your front yard?"
• Our colors for our agency are Gold and Black (the whole flyer does not need to be this color though)
• Join us for an open house in our office
• Wednesday March 1
• 3-6pm
• Back page of flyer: "If you would like to add your name to the Sold Properties list, give us a call today!
• Sold listings which we will get sent to you will also be listed on the back page.
Should not have
• do not make the flyer too "busy" with too many pictures and wording.

```html
<!DOCTYPE html>
<html lang="en">
<head>
<meta charset="utf-8">
<title>Halvorsen Realty – Open House</title>
<link href="https://fonts.googleapis.com/css2?family=Bebas+Neue&family=Roboto+Condensed:wght@300;400;700&display=swap" rel="stylesheet">
<style>
  :root{
    --orange:#e8641c;
    --orange-deep:#c9561a;
    --ink:#1e1e1e;
    --text:#2a2a2a;
    --ring:#b9b9b9;
    --frame:#3a3a3a;
    --white:#ffffff;
  }
  *{margin:0;padding:0;box-sizing:border-box}
  html,body{width:911px;height:1200px;overflow:hidden;background:var(--white)}
  .flyer{position:relative;width:911px;height:1200px;overflow:hidden;
    background:linear-gradient(180deg,#f7f7f7 0%,#e9e9e9 100%);
    font-family:"Roboto Condensed",Arial,sans-serif;color:var(--text)}

  .brand{position:absolute;top:62px;left:0;width:100%;text-align:center}
  .brand-name{font-weight:700;font-size:54px;color:var(--ink);letter-spacing:1px;line-height:1}
  .brand-tagline{margin-top:10px;font-size:20px;font-weight:400;color:var(--ink)}

  .team{position:absolute;top:205px;left:0;width:100%}
  .agent{position:absolute;width:260px;text-align:center}
  .agent:nth-child(1){left:72px}
  .agent:nth-child(2){left:331px}
  .agent:nth-child(3){left:589px}
  .agent-photo{display:block;margin:0 auto;width:240px;height:240px}
  .agent-name,.agent-role{font-family:"Bebas Neue",Arial,sans-serif;font-size:30px;line-height:34px;color:var(--ink)}
  .agent-name{margin-top:12px}

  .promo{position:absolute;top:622px;left:0;width:911px;height:453px;background:var(--orange)}
  .promo-scene{position:absolute;inset:0}

  .ribbon{position:absolute;top:567px;left:0;width:911px;height:60px}
  .headline-box{position:absolute;top:567px;left:185px;width:550px;height:292px;
    background:linear-gradient(180deg,#f4f4f4,#dcdcdc);border:7px solid var(--frame);
    text-align:center;padding-top:12px;box-shadow:0 4px 8px rgba(0,0,0,.25)}
  .headline-line{font-weight:400;font-size:64px;line-height:72px;color:var(--ink)}
  .headline-first{font-size:72px;letter-spacing:0.5px}
  .headline-strong{font-weight:700;font-size:92px;line-height:92px;color:var(--orange);letter-spacing:1px}

  .invite{position:absolute;top:888px;left:0;width:100%;text-align:center;color:var(--white)}
  .invite-lead{font-size:38px;line-height:44px;font-weight:400}
  .invite-date{font-size:40px;line-height:46px;font-weight:700}
  .invite-time{font-size:40px;line-height:48px;font-weight:400}

  .contact{position:absolute;top:1075px;left:0;width:911px;height:100px;
    background:linear-gradient(180deg,#ececec,#d6d6d6);text-align:center;padding-top:17px}
  .contact-web{font-size:30px;font-weight:700;color:var(--ink);line-height:36px}
  .contact-address{font-size:23px;color:var(--ink);line-height:28px}
  .base-strip{position:absolute;top:1175px;left:0;width:911px;height:25px;background:var(--orange)}
</style>
</head>
<body>
<div class="flyer">

  <header class="brand">
    <div class="brand-name">Halvorsen Realty LLC</div>
    <div class="brand-tagline">“Ready for your call, day or night.”</div>
  </header>

  <section class="team">
    <div class="agent">
      <svg class="agent-photo" viewBox="0 0 240 240" role="img" aria-label="Portrait photo of agent Karen Lindqvist">
        <defs><radialGradient id="pg1" cx="50%" cy="40%" r="60%"><stop offset="0" stop-color="#b89a82"/><stop offset="1" stop-color="#6e6e6e"/></radialGradient></defs>
        <circle cx="120" cy="120" r="119" fill="var(--ring)"/>
        <circle cx="120" cy="120" r="110" fill="url(#pg1)"/>
      </svg>
      <div class="agent-name">Karen Lindqvist</div>
      <div class="agent-role">Real Estate Agent</div>
    </div>
    <div class="agent">
      <svg class="agent-photo" viewBox="0 0 240 240" role="img" aria-label="Portrait photo of broker Dale Halvorsen">
        <defs><radialGradient id="pg2" cx="50%" cy="70%" r="60%"><stop offset="0" stop-color="#9a86c8"/><stop offset="1" stop-color="#6c6c6c"/></radialGradient></defs>
        <circle cx="120" cy="120" r="119" fill="var(--ring)"/>
        <circle cx="120" cy="120" r="110" fill="url(#pg2)"/>
      </svg>
      <div class="agent-name">Dale Halvorsen</div>
      <div class="agent-role">Broker</div>
    </div>
    <div class="agent">
      <svg class="agent-photo" viewBox="0 0 240 240" role="img" aria-label="Portrait photo of agent Gary Mostek">
        <defs><radialGradient id="pg3" cx="50%" cy="60%" r="60%"><stop offset="0" stop-color="#4f5660"/><stop offset="1" stop-color="#7a7a7a"/></radialGradient></defs>
        <circle cx="120" cy="120" r="119" fill="var(--ring)"/>
        <circle cx="120" cy="120" r="110" fill="url(#pg3)"/>
      </svg>
      <div class="agent-name">Gary Mostek</div>
      <div class="agent-role">Real Estate Agent</div>
    </div>
  </section>

  <section class="promo">
    <svg class="promo-scene" viewBox="0 0 911 453" preserveAspectRatio="none" role="img" aria-label="Orange-tinted photo of a large two-storey house with a front lawn">
      <defs>
        <linearGradient id="scene" x1="0" y1="0" x2="0" y2="1">
          <stop offset="0" stop-color="var(--orange)"/>
          <stop offset="0.45" stop-color="#d9611f"/>
          <stop offset="0.8" stop-color="var(--orange-deep)"/>
          <stop offset="1" stop-color="#d35e1d"/>
        </linearGradient>
      </defs>
      <rect width="911" height="453" fill="url(#scene)"/>
    </svg>
  </section>

  <svg class="ribbon" viewBox="0 0 911 60" aria-hidden="true">
    <polygon points="148,55 192,0 192,55" fill="var(--frame)"/>
    <polygon points="728,0 772,55 728,55" fill="var(--frame)"/>
  </svg>

  <div class="headline-box">
    <div class="headline-line headline-first">let us place a</div>
    <div class="headline-strong">SOLD SIGN</div>
    <div class="headline-line">in your front yard</div>
  </div>

  <section class="invite">
    <div class="invite-lead">Join us for an open house in our office</div>
    <div class="invite-date">WEDNESDAY MARCH 1</div>
    <div class="invite-time">3.00–6.00&nbsp; pm</div>
  </section>

  <footer class="contact">
    <div class="contact-web">www.halvorsenrealty.com</div>
    <div class="contact-address">48 Harbor Street | Pine Ridge, Mn 56099</div>
  </footer>
  <div class="base-strip"></div>

</div>
</body>
</html>
```